Bellmoor Commercial Finance Information Brochure

This brochure will be sent out to clients via A4 PDF on an email to showcase what our company has to offer. We are a commercial finance brokerage, that specialises in property finance. We would like to see designs following our colour scheme. The final design should demonstrate our professionalism and reliability.
I have attached our logo and also a few bullet points on our information and what we can offer. These can be slightly reworded for conciseness. Or leave the text sections as filler and I can fill these in.
I have also attached an overview of our colour scheme and design styling for your consideration.
Target Market(s)
Property Developers
Industry/Entity Type
Financial Services

```html
<!DOCTYPE html>
<html lang="en">
<head>
<meta charset="utf-8">
<title>Bellmoor Finance – Brochure Cover</title>
<link href="https://fonts.googleapis.com/css2?family=Montserrat:wght@700;800&family=Open+Sans:wght@400;600&display=swap" rel="stylesheet">
<style>
  :root{
    --bg:#e4e4e6;
    --ink-dark:#1b1d20;
    --brand-blue:#1c3fa3;
    --brand-blue-deep:#0f2d86;
    --brand-green:#1f8a3c;
    --paper:#f6f6f6;
    --white:#ffffff;
    --building-a:#3a4756;
    --building-b:#1f2731;
    --handshake-a:#c9d6e6;
    --handshake-b:#8b98aa;
    --city-a:#2f8a43;
    --city-b:#1c6a30;
  }
  *{margin:0;padding:0;box-sizing:border-box}
  html,body{width:1200px;height:840px;overflow:hidden;background:var(--bg)}
  .canvas{position:relative;width:1200px;height:840px}
  .page{position:absolute;top:40px;width:537px;height:760px;overflow:hidden;box-shadow:0 6px 18px rgba(0,0,0,.18)}
  .page--back{left:63px;background:var(--ink-dark)}
  .page--front{left:600px;background:var(--paper)}
  .page svg.layer{position:absolute;inset:0;width:100%;height:100%}

  .photo-team{position:absolute;inset:0;background:linear-gradient(160deg,#2a2c30 0%,#17181b 60%,#111214 100%)}

  .wordmark{font-family:"Montserrat",sans-serif;font-weight:800;letter-spacing:.06em;color:var(--brand-blue);line-height:1;text-transform:uppercase;display:flex;align-items:center;gap:10px}
  .wordmark__dot{width:12px;height:12px;background:var(--brand-green);flex:none}

  .back-brand{position:absolute;top:120px;left:0;width:100%;display:flex;justify-content:center}
  .back-brand .wordmark{font-size:30px}

  .contact{position:absolute;top:230px;left:0;width:100%;text-align:center;font-family:"Open Sans",sans-serif;color:var(--white);font-size:15px;line-height:1.4}
  .contact__item{margin-bottom:16px}
  .contact__icon{display:block;margin:0 auto 6px;width:18px;height:18px}

  .headline{position:absolute;left:34px;top:230px;font-family:"Montserrat",sans-serif;font-weight:800;color:var(--white);font-size:44px;line-height:1.02;text-transform:uppercase;letter-spacing:.02em}

  .front-brand{position:absolute;left:262px;top:548px}
  .front-brand .wordmark{font-size:28px}
</style>
</head>
<body>
<main class="canvas">

  <section class="page page--back">
    <div class="photo-team" role="img" aria-label="Dark-toned photo of a team stacking hands over a desk of documents"></div>
    <svg class="layer" viewBox="0 0 537 760" preserveAspectRatio="none" aria-hidden="true">
      <path d="M0 575 Q250 690 537 690 L537 760 L0 760Z" fill="var(--brand-green)"/>
      <path d="M0 585 Q250 698 537 698 L537 760 L0 760Z" fill="var(--white)"/>
      <path d="M0 595 Q250 706 537 706 L537 760 L0 760Z" fill="var(--brand-blue-deep)"/>
    </svg>

    <div class="back-brand">
      <div class="wordmark"><span class="wordmark__dot"></span>Bellmoor Finance</div>
    </div>

    <address class="contact" style="font-style:normal">
      <div class="contact__item">
        <svg class="contact__icon" viewBox="0 0 24 24"><path d="M12 2a7 7 0 0 0-7 7c0 5 7 13 7 13s7-8 7-13a7 7 0 0 0-7-7zm0 9.5A2.5 2.5 0 1 1 12 6.5a2.5 2.5 0 0 1 0 5z" fill="var(--brand-green)"/></svg>
        1820 Linden Row<br>Fairhaven, Ohio 45210
      </div>
      <div class="contact__item">
        <svg class="contact__icon" viewBox="0 0 24 24"><path d="M6.6 10.8a15 15 0 0 0 6.6 6.6l2.2-2.2a1 1 0 0 1 1-.25 11.4 11.4 0 0 0 3.6.57 1 1 0 0 1 1 1V20a1 1 0 0 1-1 1A17 17 0 0 1 3 4a1 1 0 0 1 1-1h3.5a1 1 0 0 1 1 1c0 1.25.2 2.45.57 3.57a1 1 0 0 1-.25 1z" fill="var(--brand-green)"/></svg>
        555-210-4187<br>555-210-4932
      </div>
      <div class="contact__item">
        <svg class="contact__icon" viewBox="0 0 24 24"><path d="M3 5h18v14H3z" fill="var(--brand-green)"/><path d="M3 5l9 7 9-7" fill="none" stroke="var(--ink-dark)" stroke-width="1.6"/></svg>
        info@bellmoorfinance.com
      </div>
      <div class="contact__item">
        <svg class="contact__icon" viewBox="0 0 24 24"><circle cx="12" cy="12" r="10" fill="var(--brand-green)"/><path d="M2 12h20M12 2c3 3 3 17 0 20M12 2c-3 3-3 17 0 20" fill="none" stroke="var(--ink-dark)" stroke-width="1.2"/></svg>
        www.bellmoorfinance.com
      </div>
    </address>
  </section>

  <section class="page page--front">
    <svg class="layer" viewBox="0 0 537 760" preserveAspectRatio="none">
      <defs>
        <linearGradient id="gradBuilding" x1="0" y1="0" x2="1" y2="1">
          <stop offset="0" stop-color="var(--building-a)"/><stop offset="1" stop-color="var(--building-b)"/>
        </linearGradient>
        <linearGradient id="gradHandshake" x1="0" y1="0" x2="1" y2="1">
          <stop offset="0" stop-color="var(--handshake-a)"/><stop offset="1" stop-color="var(--handshake-b)"/>
        </linearGradient>
        <linearGradient id="gradCity" x1="0" y1="0" x2="1" y2="1">
          <stop offset="0" stop-color="var(--city-a)"/><stop offset="1" stop-color="var(--city-b)"/>
        </linearGradient>
      </defs>
      <polygon points="0,0 140,0 330,410 120,650 0,650" fill="url(#gradBuilding)" role="img" aria-label="Photo looking up a glass office tower"/>
      <polygon points="190,0 537,0 537,320 345,395" fill="url(#gradHandshake)" role="img" aria-label="Photo of two business people shaking hands"/>
      <polygon points="365,440 537,385 537,580 478,635" fill="url(#gradCity)" role="img" aria-label="Green-toned photo of a city skyline"/>
      <path d="M0 640 Q280 690 537 700 L537 760 L0 760Z" fill="var(--brand-green)"/>
      <path d="M0 650 Q280 700 537 710 L537 760 L0 760Z" fill="var(--white)"/>
      <path d="M0 658 Q280 708 537 718 L537 760 L0 760Z" fill="var(--brand-blue)"/>
    </svg>

    <h1 class="headline">We<br>will<br>do the<br>best<br>for your<br>furture</h1>

    <div class="front-brand">
      <div class="wordmark"><span class="wordmark__dot"></span>Bellmoor Finance</div>
    </div>
  </section>

</main>
</body>
</html>
```